Fruit and veg boxes + online deli

I need a flyer that showcases my four different types of fruit and veg boxes: small £8.50, medium &14, large £19.50, build your own box -(minimum spend is £5/each item is individually priced).
It must also illustrate my online deli feature. We sell cheeses, meat, fish, gourmet pies, tray bakes and bread baked in house.
Folded A4 horizontal leaflet, so four sided.
We're a small UK start up online green grocer.
We promote our service by offering a free trial box (small box only). The design must focus heavily on this.
We promote local and regional agriculture.

Target Market(s)

All residential households

Font styles to use
Decorative

Requirements
Must have
• Here is my website so you can get the general feel of my service
• www.plumcrateorchard.co.uk
• Cover page must emphasize heavily on our free trial offer.
• Our 4 different types of boxes on page 2
• Our deli on page 3/4
• Our contact details / website visible on pages 2/3/4
Nice to have
• Nice to tell the reader that we're a small UK start up online greengrocer.
• We offer a different alternative to supermarket shopping by offering hand made delicatessen..

```html
<!DOCTYPE html>
<html lang="en">
<head>
<meta charset="utf-8">
<title>Plum Crate Orchard – Leaflet</title>
<link href="https://fonts.googleapis.com/css2?family=Libre+Baskerville:wght@400;700&family=Crimson+Text:wght@400;600&family=Open+Sans:wght@400;600&display=swap" rel="stylesheet">
<style>
  :root{
    --backdrop:#5b5d5c;
    --paper:#e6e6e1;
    --charcoal:#333333;
    --white:#ffffff;
    --ink:#3a3a3a;
    --muted:#6f6f6c;
    --icon:#a9a9a6;
    --coral:#ea6148;
    --leaf:#3cb46e;
  }
  *{margin:0;padding:0;box-sizing:border-box}
  html,body{width:848px;height:1200px;overflow:hidden;background:var(--backdrop)}
  body{position:relative;font-family:"Crimson Text",Georgia,serif;color:var(--ink)}
  .abs{position:absolute}

  /* Outer spread */
  .spread-outer{left:55px;top:62px;width:738px;height:522px;background:var(--paper);overflow:hidden}
  .photo-produce{left:0;top:0;width:184px;height:522px;
    background:linear-gradient(160deg,#a9522b 0%,#7a8a3c 35%,#c23a2a 55%,#8a3040 78%,#b0702e 100%)}
  .cover-frame{left:19px;top:11px;width:338px;height:488px;border:2px solid var(--white)}
  .contact-card{left:214px;top:265px;width:128px;height:138px;border:2px solid var(--white);padding:8px}
  .contact-inner{width:100%;height:100%;background:var(--white);text-align:center;padding-top:14px}
  .contact-title{font-family:"Libre Baskerville",serif;font-size:10.5px;letter-spacing:.5px;color:var(--ink)}
  .contact-label{font-family:"Libre Baskerville",serif;font-size:7px;color:var(--coral);margin-top:17px}
  .contact-value{font-size:5.5px;color:var(--muted);margin-top:3px;white-space:nowrap}
  .barn{left:271px;top:428px}
  .base-line{left:195px;top:480px;width:166px;height:1px;background:var(--icon)}
  .photo-berries{left:373px;top:0;width:184px;height:522px;
    background:linear-gradient(175deg,#3d4a63 0%,#4c5a72 30%,#b32a38 45%,#5b6273 60%,#474f5e 100%)}
  .brand-box{left:415px;top:84px;width:284px;height:84px;background:var(--white);text-align:center;padding-top:20px}
  .brand-name{font-family:"Libre Baskerville",serif;font-size:24px;color:var(--ink);letter-spacing:.3px;white-space:nowrap}
  .brand-strap{font-size:7.5px;color:var(--muted);margin-top:8px;letter-spacing:.4px;white-space:nowrap}
  .tag-box{left:415px;top:175px;width:284px;height:29px;border:2px solid var(--white);background:var(--white);
    font-size:9.5px;color:var(--ink);padding:6px 0 0 10px;outline:1px solid var(--ink);outline-offset:-4px;white-space:nowrap}
  .startup-box{left:415px;top:207px;width:128px;height:34px;border:2px solid var(--white);
    font-size:9px;font-weight:600;color:var(--white);line-height:1.25;padding:3px 8px}
  .trial-box{left:415px;top:252px;width:170px;height:50px;background:var(--coral);color:var(--white);
    text-align:center;padding-top:7px}
  .trial-main{font-family:"Libre Baskerville",serif;font-weight:700;font-size:14px;letter-spacing:.4px}
  .trial-sub{font-size:9.5px;margin-top:3px}
  .icon-rail{left:600px;top:306px;width:1px;height:216px;background:var(--icon)}
  .icon-strip{left:563px;top:318px;width:30px;height:182px;background:linear-gradient(#dcdcd7,#d3d3cd);opacity:.9}
  .farm-scene{left:605px;top:400px;width:100px;height:100px;background:linear-gradient(#e6e6e1,#d2d2cc)}
  .fence{left:557px;top:506px;width:130px;height:16px;
    background:repeating-linear-gradient(90deg,var(--icon) 0 1px,transparent 1px 4px)}
  .sprig{left:703px;top:348px}
  .deli-tab{left:686px;top:384px;width:52px;height:138px;background:var(--coral)}
  .deli-tab-text{position:absolute;left:50%;top:50%;transform:translate(-50%,-50%) rotate(-90deg);
    white-space:nowrap;font-family:"Open Sans",sans-serif;color:var(--white);text-align:left;line-height:1.05}
  .deli-tab-text .big{font-size:15px;display:block}
  .deli-tab-text .small{font-size:8px;display:block}

  /* Inner spread */
  .spread-inner{left:55px;top:616px;width:738px;height:521px;background:var(--paper);overflow:hidden}
  .deli-panel{left:0;top:0;width:368px;height:521px;background:var(--charcoal)}
  .deli-frame{left:16px;top:14px;width:353px;height:487px;border:2px solid var(--white);border-right:none}
  .deli-title{left:0;width:368px;top:28px;text-align:center;font-family:"Libre Baskerville",serif;font-size:19px;color:var(--white)}
  .deli-intro{left:52px;width:300px;top:72px;text-align:center;font-size:9.6px;line-height:1.3;color:var(--white)}
  .deli-item{width:110px;text-align:center;font-family:"Libre Baskerville",serif;font-weight:700;font-size:8.6px;line-height:1.5;color:#d8d8d5}
  .deli-icon{display:block;margin:0 auto 6px;width:32px;height:28px;border-radius:5px;background:var(--icon)}
  .deli-more{left:0;width:368px;top:428px;text-align:center;font-family:"Libre Baskerville",serif;font-size:10.5px;color:var(--white)}
  .deli-url{left:0;width:368px;top:448px;text-align:center;font-family:"Libre Baskerville",serif;font-size:10.5px;color:var(--coral)}

  .boxes-title{left:368px;width:370px;top:30px;text-align:center;font-family:"Libre Baskerville",serif;font-weight:700;font-size:18px;color:var(--leaf);letter-spacing:.5px}
  .box-card{width:166px;text-align:center}
  .box-name{font-family:"Libre Baskerville",serif;font-size:12px;color:var(--ink);white-space:nowrap}
  .box-detail{font-size:10.5px;line-height:1.33;color:var(--muted);margin-top:7px}
  .crate-art{left:442px;top:200px;width:228px;height:100px;background:linear-gradient(#d7e9dc,#c8e3d1);border-radius:4px}
  .free-offer{left:368px;width:370px;top:460px;text-align:center;font-family:"Libre Baskerville",serif;font-size:12px;color:var(--coral)}
</style>
</head>
<body>

<section class="abs spread-outer" aria-label="Outside spread: back and cover">
  <div class="abs photo-produce" role="img" aria-label="Photograph of a wooden crate of fresh vegetables and fruit"></div>
  <div class="abs cover-frame"></div>
  <div class="abs contact-card">
    <div class="contact-inner">
      <div class="contact-title">CONTACT US</div>
      <div class="contact-label">WEBSITE</div>
      <div class="contact-value">plumcrateorchard.co.uk</div>
      <div class="contact-label" style="margin-top:14px">EMAIL</div>
      <div class="contact-value">info@plumcrateorchard.co.uk</div>
    </div>
  </div>
  <svg class="abs barn" width="56" height="54" viewBox="0 0 56 54" aria-hidden="true">
    <polygon points="28,4 4,26 4,52 52,52 52,26" fill="var(--icon)"/>
    <rect x="25" y="0" width="6" height="8" fill="var(--icon)"/>
    <rect x="20" y="34" width="16" height="18" fill="var(--paper)"/>
    <rect x="22" y="20" width="12" height="5" fill="var(--paper)"/>
  </svg>
  <div class="abs base-line"></div>

  <div class="abs photo-berries" role="img" aria-label="Photograph of blueberries and raspberries in bowls on rustic wooden boards"></div>
  <div class="abs brand-box">
    <div class="brand-name">Plum Crate Orchard</div>
    <div class="brand-strap">Bringing you the very best fruit &amp; veg direct to your doorstep</div>
  </div>
  <div class="abs tag-box">Our fruit and vegetable boxes are full of farm fresh goodness</div>
  <div class="abs startup-box">small UK start up online greengrocer</div>
  <div class="abs trial-box">
    <div class="trial-main">FREE TRIAL BOX</div>
    <div class="trial-sub">Your first small box is on us</div>
  </div>

  <div class="abs icon-strip" role="img" aria-label="Column of small grey food pictograms"></div>
  <div class="abs icon-rail"></div>
  <div class="abs farm-scene" role="img" aria-label="Grey illustration of a fish above a tractor"></div>
  <div class="abs fence"></div>
  <svg class="abs sprig" width="22" height="28" viewBox="0 0 22 28" aria-hidden="true">
    <ellipse cx="11" cy="6" rx="3.5" ry="6" fill="var(--icon)"/>
    <ellipse cx="5" cy="15" rx="3.5" ry="6" transform="rotate(-30 5 15)" fill="var(--icon)"/>
    <ellipse cx="17" cy="15" rx="3.5" ry="6" transform="rotate(30 17 15)" fill="var(--icon)"/>
    <rect x="10" y="14" width="2" height="14" fill="var(--icon)"/>
  </svg>
  <div class="abs deli-tab">
    <div class="deli-tab-text"><span class="big">Online Deli</span><span class="small">details inside</span></div>
  </div>
</section>

<section class="abs spread-inner" aria-label="Inside spread: deli and boxes">
  <div class="abs deli-panel"></div>
  <div class="abs deli-frame"></div>
  <h2 class="abs deli-title">Online Deli</h2>
  <p class="abs deli-intro">You can also choose to have any of the following products to be delivered alongside your fruit and veg box.<br>Our online deli features many award winning foods. Plenty to choose from.</p>

  <div class="abs deli-item" style="left:50px;top:156px"><span class="deli-icon" role="img" aria-label="Cheese icon"></span>Bread,<br>Eggs &amp; Dairy</div>
  <div class="abs deli-item" style="left:142px;top:156px"><span class="deli-icon" role="img" aria-label="Soup bowl icon"></span>Fruit<br>Juices &amp; Soups</div>
  <div class="abs deli-item" style="left:226px;top:156px"><span class="deli-icon" role="img" aria-label="Roast chicken icon"></span>My<br>Meat Box</div>
  <div class="abs deli-item" style="left:50px;top:251px"><span class="deli-icon" role="img" aria-label="Coffee beans icon"></span>Tea,Coffee,<br>Biscuits &amp; Cereals</div>
  <div class="abs deli-item" style="left:142px;top:251px"><span class="deli-icon" role="img" aria-label="Jar icon"></span>Jams,<br>Curds &amp; Honey</div>
  <div class="abs deli-item" style="left:226px;top:251px"><span class="deli-icon" role="img" aria-label="Fish icon"></span>Fish<br>&nbsp;</div>
  <div class="abs deli-item" style="left:50px;top:333px"><span class="deli-icon" role="img" aria-label="Bottles icon"></span>Cooking Sauces<br>&amp; Condiments</div>
  <div class="abs deli-item" style="left:142px;top:333px"><span class="deli-icon" role="img" aria-label="Herb sprig icon"></span>Herbs &amp; More<br>Fresh Produce</div>
  <div class="abs deli-item" style="left:226px;top:333px"><span class="deli-icon" role="img" aria-label="Gift box icon"></span>Weekend<br>Treats &amp; Snacks</div>

  <div class="abs deli-more">view more at our website</div>
  <div class="abs deli-url">plumcrateorchard.co.uk</div>

  <h2 class="abs boxes-title">Pre - Packed Boxes</h2>
  <div class="abs box-card" style="left:383px;top:72px">
    <div class="box-name">Large Box | £19.50</div>
    <div class="box-detail">Suitable for 4-6 peole<br>Available as<br>Fruit only<br>Veg only<br>Mixed Fruit &amp; Veg</div>
  </div>
  <div class="abs box-card" style="left:557px;top:72px">
    <div class="box-name">Medium Box | £14.00</div>
    <div class="box-detail">Suitable for 2-4 peole<br>Available as<br>Fruit only<br>Veg only<br>Mixed Fruit &amp; Veg</div>
  </div>
  <div class="abs crate-art" role="img" aria-label="Green line illustration of a crate overflowing with fruit and vegetables"></div>
  <div class="abs box-card" style="left:383px;top:340px">
    <div class="box-name">Small Box | £8.50</div>
    <div class="box-detail">Suitable for 1-2 peole<br>Available as<br>Fruit only<br>Veg only<br>Mixed Fruit &amp; Veg</div>
  </div>
  <div class="abs box-card" style="left:557px;top:340px">
    <div class="box-name">Build Your Own | £5.00</div>
    <div class="box-detail">Minimum spend £5<br>Each item is<br>individually priced<br>Pick any fruit<br>&amp; veg you like</div>
  </div>
  <p class="abs free-offer">Receive your first small box from us for FREE</p>
</section>

</body>
</html>
```